Lanterns On Loan (Tattoo Shop)

its for a business sign that is 8 foot by 22 inches looking for a classy modern black and white (Maybe some gold) easy to read sign. As you can see there is some very poor boarders added, please add what you think will look good. ITs for a tattoo shop. Maybe shoot one or two of the desgins with a fillagree look, still keeping it simple.

Target Market(s)

beginner and veteran tattoo collectors, leaving behind the old back door biker shop and stepping into the new age of tattooing. Looking to attract all types and make clients feel comfortable getting large pieces

Industry/Entity Type

Tattoo

Logo Text

Lanterns On Loan

Font styles to use
Decorative
Other font styles liked:
• Modern

Colors
000000
959595
eaeaea
d3d3d3
ffffff

Requirements
Must have
• Lanterns On Loan (words), using as much space as you can. Be black and white in color and a few samples in gold. Have the proper dimension easily legible. Some boarders.
Nice to have
• using the number of designs wisely if you think of something that will look good feel free to add it. Adding a few sample for shades of grey only color I would want added is gold ( fairly certain on black and white but I would like to see one or tow with gold)
• Maybe one example of decorative

```html
<!DOCTYPE html>
<html lang="en">
<head>
<meta charset="utf-8">
<title>Lanterns On Loan – Shop Sign</title>
<link rel="stylesheet" href="https://fonts.googleapis.com/css2?family=New+Rocker&display=swap">
<style>
  :root {
    --backdrop: #d3d3d3;
    --sign-black: #000000;
    --gold-light: #f7d34a;
    --gold-mid: #d99a1e;
    --gold-deep: #8a4a12;
    --frame-line: #b88a2a;
  }
  html, body {
    margin: 0;
    padding: 0;
    width: 1200px;
    height: 1200px;
    overflow: hidden;
    background: var(--backdrop);
  }
  .canvas {
    width: 1200px;
    height: 1200px;
    display: flex;
    align-items: center;
    justify-content: center;
  }
  .sign {
    position: relative;
    width: 1100px;
    height: 252px;
    background: var(--sign-black);
    overflow: hidden;
  }
  .sign-frame {
    position: absolute;
    inset: 16px;
    border: 1px solid var(--frame-line);
  }
  .filigree {
    position: absolute;
    background: radial-gradient(ellipse at center, var(--gold-light) 0%, var(--gold-mid) 45%, var(--gold-deep) 80%, transparent 100%);
    opacity: 0.85;
  }
  .filigree--top-left {
    top: 0;
    left: 60px;
    width: 130px;
    height: 26px;
    border-radius: 0 0 60px 60px;
  }
  .filigree--bottom-right {
    bottom: 0;
    right: 120px;
    width: 170px;
    height: 34px;
    border-radius: 60px 60px 0 0;
  }
  .sign-name {
    position: absolute;
    inset: 0;
    display: flex;
    align-items: center;
    justify-content: center;
    margin: 0;
    padding: 0 50px;
    white-space: nowrap;
    font-family: "New Rocker", fantasy;
    font-weight: 400;
    font-size: 82px;
    letter-spacing: 1px;
    text-transform: uppercase;
    line-height: 1;
    background: linear-gradient(180deg, var(--gold-deep) 30%, var(--gold-mid) 42%, var(--gold-light) 52%, var(--gold-mid) 60%, var(--gold-deep) 72%);
    -webkit-background-clip: text;
    background-clip: text;
    color: transparent;
  }
</style>
</head>
<body>
  <main class="canvas">
    <section class="sign">
      <div class="sign-frame"></div>
      <div class="filigree filigree--top-left" role="img" aria-label="Gold filigree corner ornament"></div>
      <div class="filigree filigree--bottom-right" role="img" aria-label="Gold filigree scroll ornament"></div>
      <h1 class="sign-name">Lanterns On Loan</h1>
    </section>
  </main>
</body>
</html>
```